Bright, Fun and hard to forget home inspection business card.

We need a Business card design for a new Home Inspection company. We are building a brand that is bright, fun and easy to remember.

Target Market(s)

Anyone involed in buying and selling of homes.

Industry/Entity Type

Home Inspection

Contact Information for Business Card

Colin Marlowe Owner/Inspector

Wedsite- PorchAndRafterCheck.example
Phone: 253-555-0187
Email- ColinMarlowe@mailbox.example
WA Lic # 4806

Requirements
Must have
• BRQV LOGO somewhere on card.

```html
<!DOCTYPE html>
<html lang="en">
<head>
<meta charset="utf-8">
<title>Porch And Rafter Check – Business Card</title>
<link href="https://fonts.googleapis.com/css2?family=Oswald:wght@300;400;500;600&display=swap" rel="stylesheet">
<style>
  :root {
    --orange: #f15a2b;
    --orange-soft: #f58a68;
    --orange-pale: #fbb49c;
    --ink: #231f20;
    --paper: #ffffff;
    --backdrop: #45494c;
  }
  * { margin: 0; padding: 0; box-sizing: border-box; }
  html, body { width: 1200px; height: 1000px; overflow: hidden; }
  body {
    background: var(--backdrop);
    position: relative;
    font-family: "Oswald", "Arial Narrow", sans-serif;
  }
  .card {
    position: absolute;
    width: 502px;
    height: 288px;
    overflow: hidden;
  }

  /* Front side */
  .card-front { left: 340px; top: 112px; background: var(--paper); }
  .front-band {
    position: absolute; left: 0; top: 0; width: 100%; height: 78px;
    background: var(--orange);
  }
  .holder-name {
    position: absolute; right: 194px; top: 4px;
    font-weight: 500; font-size: 40px; line-height: 1.1;
    color: var(--paper); letter-spacing: 0.5px; text-transform: uppercase;
    transform: scaleX(0.82); transform-origin: right top;
  }
  .holder-role {
    position: absolute; right: 194px; top: 52px;
    font-weight: 300; font-size: 13px; color: var(--orange-pale);
    text-transform: uppercase; letter-spacing: 0.3px;
  }
  .mascot-panel {
    position: absolute; left: 306px; top: 0; width: 196px; height: 288px;
    background: var(--orange);
    border-radius: 90px 0 0 60px;
  }
  .contact-list { position: absolute; left: 41px; top: 110px; list-style: none; }
  .contact-row { display: flex; align-items: center; height: 44px; }
  .contact-label {
    width: 49px; height: 19px; border-radius: 10px;
    background: var(--orange); color: var(--paper);
    font-weight: 300; font-size: 12px; line-height: 19px; text-align: center;
  }
  .contact-value {
    margin-left: 25px; font-weight: 400; font-size: 15px; color: var(--ink);
    letter-spacing: 0.3px;
  }

  /* Back side */
  .card-back { left: 338px; top: 583px; background: var(--orange); }
  .backdrop-mark {
    position: absolute; left: 240px; top: 0; width: 262px; height: 288px;
    background: linear-gradient(160deg, var(--orange-soft) 0%, rgba(245,138,104,0.35) 70%, var(--orange) 100%);
    border-radius: 120px 0 0 0;
  }
  .brand-lockup {
    position: absolute; left: 34px; top: 96px;
    display: flex; align-items: center; gap: 10px;
  }
  .mascot-badge {
    width: 122px; height: 150px; border-radius: 40px;
    background: var(--paper);
  }
  .brand-name {
    font-weight: 400; font-size: 30px; line-height: 1.0;
    color: var(--paper); text-transform: uppercase;
  }
</style>
</head>
<body>
  <section class="card card-front" aria-label="Business card front">
    <div class="front-band"></div>
    <div class="mascot-panel" role="img" aria-label="Illustrated mascot holding a megaphone"></div>
    <h1 class="holder-name">Colin Marlowe</h1>
    <p class="holder-role">Owner | Inspector</p>
    <ul class="contact-list">
      <li class="contact-row"><span class="contact-label">phone</span><span class="contact-value">253.555.0187</span></li>
      <li class="contact-row"><span class="contact-label">email</span><span class="contact-value">ColinMarlowe@mailbox.example</span></li>
      <li class="contact-row"><span class="contact-label">web</span><span class="contact-value">PorchAndRafterCheck.example</span></li>
      <li class="contact-row"><span class="contact-label">wa lic</span><span class="contact-value"># 4806</span></li>
    </ul>
  </section>

  <section class="card card-back" aria-label="Business card back">
    <div class="backdrop-mark" role="img" aria-label="Large faint mascot decoration"></div>
    <div class="brand-lockup">
      <div class="mascot-badge" role="img" aria-label="Mascot illustration"></div>
      <p class="brand-name">Porch And<br>Rafter<br>Check LLC</p>
    </div>
  </section>
</body>
</html>
```